Online trading school - Website design

We are building an online trading school (trading of shares, commodities, indices, currencies). The purpose is to teach online traders how to trade successfully. We need to design the homepage of the website and logo (bramwelloq.com will be the domain). The homepage will contain the following elements

- logo
- Sign in and Register links/buttons
- upper menu
- short introduction
- a couple of bullet points 'Why to join our school?'
- sign up form
- text
- bottom menu

Attached is a draft for the designer. The draft is just for an inspiration, the actual structure of the website can be different if the designer thinks so.

The designer is free to choose colors.

School

3 page

```html
<!DOCTYPE html>
<html lang="en">
<head>
<meta charset="utf-8">
<title>Bramwelloq – Online Trading School</title>
<link href="https://fonts.googleapis.com/css2?family=Open+Sans:wght@300;400;600&family=Libre+Baskerville&display=swap" rel="stylesheet">
<style>
:root{
  --ink:#2b2f30;
  --muted:#8a8f90;
  --teal:#3e6d70;
  --teal-light:#6fb5b5;
  --aqua:#7fd3d0;
  --dark:#1f2526;
  --darker:#151a1b;
  --line:#d9dcdc;
  --white:#ffffff;
}
*{box-sizing:border-box;margin:0;padding:0}
html,body{width:1200px;height:2444px;overflow:hidden}
body{font-family:"Open Sans",Arial,sans-serif;color:var(--ink);background:var(--white)}

/* header */
.site-header{height:144px;position:relative;background:var(--white)}
.brand{position:absolute;left:60px;top:40px;display:flex;align-items:center;gap:14px;
  font-size:40px;font-weight:400;color:var(--ink)}
.brand-mark{width:14px;height:14px;background:var(--teal)}
.account-links{position:absolute;right:60px;top:18px;display:flex;gap:22px;font-size:14px;align-items:center}
.account-links span{display:flex;align-items:center;gap:6px}
.account-links .dot{width:12px;height:12px;background:var(--teal)}
.main-nav{position:absolute;right:60px;top:76px;display:flex;gap:30px;font-size:16px}

/* hero */
.hero{height:656px;position:relative;
  background:linear-gradient(180deg,#5e6263 0%,#9fa3a4 45%,#e8eaea 100%)}
.hero-photo{position:absolute;inset:0}
.hero-title{position:absolute;left:0;right:0;top:450px;text-align:center;
  font-family:"Libre Baskerville",Georgia,serif;font-size:44px;line-height:58px;color:var(--teal-light)}

/* welcome */
.welcome{height:440px;padding:44px 84px 0;text-align:center}
.section-title{font-weight:300;font-size:40px;color:var(--ink)}
.divider{width:560px;margin:14px auto 0;height:12px;position:relative}
.divider::before{content:"";position:absolute;left:0;right:0;top:5px;border-top:1px solid var(--line)}
.divider::after{content:"";position:absolute;left:270px;top:0;width:20px;height:12px;background:var(--teal);
  clip-path:polygon(0 0,100% 0,50% 100%)}
.welcome p{font-size:14px;line-height:24px;color:var(--muted);margin-top:30px}
.welcome p + p{margin-top:20px}
.btn{display:inline-block;background:var(--teal);color:var(--white);font-size:14px;
  padding:10px 34px;margin-top:44px}

/* join */
.join{height:580px;position:relative;
  background:linear-gradient(120deg,var(--darker) 0%,#2c3435 50%,var(--dark) 100%)}
.why{position:absolute;left:80px;top:80px;width:440px}
.join h2{font-weight:300;font-size:36px;color:var(--white)}
.join .rule{border-top:1px solid #4b5556;margin-top:14px}
.why ul{list-style:none;margin-top:30px}
.why li{display:flex;align-items:center;gap:14px;color:var(--white);font-size:16px;height:37px}
.why svg{width:18px;height:18px}
.signup{position:absolute;left:640px;top:80px;width:480px}
.signup .field{width:380px;height:44px;background:var(--white);margin-top:16px;
  font-size:13px;color:var(--muted);padding:13px 16px}
.signup .field:first-of-type{margin-top:34px}
.agree{display:flex;align-items:center;gap:10px;color:var(--white);font-size:13px;margin-top:20px}
.agree i{width:14px;height:14px;background:var(--white);display:block}
.submit{display:inline-block;background:var(--aqua);color:var(--white);font-size:14px;
  padding:12px 40px;margin-top:22px}

/* offer */
.offer{height:568px;padding-top:44px;text-align:center}
.cards{display:flex;gap:28px;margin:44px 80px 0}
.card{width:240px;border:1px solid var(--line);padding-bottom:22px}
.card-photo{height:164px}
.card h3{font-weight:400;font-size:17px;margin-top:22px}
.card p{font-size:12px;line-height:18px;color:var(--muted);margin:10px 26px 0}
.card .more{font-size:12px;color:var(--muted);margin-top:10px}
.photo-shares{background:linear-gradient(135deg,#1b5fb0,#6fb6ea)}
.photo-commodities{background:linear-gradient(135deg,#3b2a10,#c9932f)}
.photo-indices{background:linear-gradient(135deg,#6d8f4e,#d5d8b0)}
.photo-currencies{background:linear-gradient(135deg,#8f8a7a,#d8d3c2)}

/* footer */
.site-footer{height:56px;background:var(--darker);color:var(--white);font-size:14px;
  display:flex;justify-content:center;align-items:center;gap:24px}
</style>
</head>
<body>
<header class="site-header">
  <div class="brand"><span class="brand-mark"></span>Bramwelloq</div>
  <div class="account-links">
    <span><i class="dot"></i>Sign in</span>
    <span><i class="dot"></i>Register</span>
  </div>
  <nav class="main-nav">
    <span>Home</span><span>About Our School</span><span>Risk Warning</span>
    <span>FAQ</span><span>Trading Glossary</span><span>Contact</span>
  </nav>
</header>

<section class="hero">
  <div class="hero-photo" role="img" aria-label="Black and white photo of a delighted trader celebrating at his desk"></div>
  <h1 class="hero-title">Become A<br>Successful Trader<br>With Bramwelloq</h1>
</section>

<section class="welcome">
  <h2 class="section-title">Welcome To Bramwelloq</h2>
  <div class="divider"></div>
  <p>Our school teaches traders of every level how markets move, how to read price action and how to manage risk with discipline. Each course combines short video lessons, live sessions with experienced mentors and practical exercises you can apply at once. You learn at your own pace, from any device, and keep lifetime access to every lesson you complete.</p>
  <p>Whether you want to trade shares, commodities, indices or currencies, our structured programme guides you from the first principles to a complete trading plan. Join a community of motivated students, test your ideas on a demo account and build the confidence to trade with a clear strategy.</p>
  <span class="btn">Read More</span>
</section>

<section class="join">
  <div class="why">
    <h2>Why To Join Us?</h2>
    <div class="rule"></div>
    <ul>
      <li><svg viewBox="0 0 18 18"><path d="M2 9l5 5 9-11" fill="none" stroke="#fff" stroke-width="2.5"/></svg>Best Trading Tips Ever</li>
      <li><svg viewBox="0 0 18 18"><path d="M2 9l5 5 9-11" fill="none" stroke="#fff" stroke-width="2.5"/></svg>Secret Tips From Experts</li>
      <li><svg viewBox="0 0 18 18"><path d="M2 9l5 5 9-11" fill="none" stroke="#fff" stroke-width="2.5"/></svg>We Teach You How To Trade Online</li>
      <li><svg viewBox="0 0 18 18"><path d="M2 9l5 5 9-11" fill="none" stroke="#fff" stroke-width="2.5"/></svg>Learn How To Trade Commodities</li>
      <li><svg viewBox="0 0 18 18"><path d="M2 9l5 5 9-11" fill="none" stroke="#fff" stroke-width="2.5"/></svg>Learn How To Become A Trader</li>
      <li><svg viewBox="0 0 18 18"><path d="M2 9l5 5 9-11" fill="none" stroke="#fff" stroke-width="2.5"/></svg>Fusce semper ex non mauris varius</li>
      <li><svg viewBox="0 0 18 18"><path d="M2 9l5 5 9-11" fill="none" stroke="#fff" stroke-width="2.5"/></svg>Learn How To Trade Commodities</li>
      <li><svg viewBox="0 0 18 18"><path d="M2 9l5 5 9-11" fill="none" stroke="#fff" stroke-width="2.5"/></svg>We Teach You How To Trade Online</li>
    </ul>
  </div>
  <form class="signup">
    <h2>Join Our School Now!</h2>
    <div class="rule"></div>
    <div class="field">First Name</div>
    <div class="field">Last Name</div>
    <div class="field">Email Address</div>
    <div class="agree"><i></i>I agree With Our Terms &amp; Conditions</div>
    <span class="submit">Submit</span>
  </form>
</section>

<section class="offer">
  <h2 class="section-title">We Offer</h2>
  <div class="divider"></div>
  <div class="cards">
    <article class="card">
      <div class="card-photo photo-shares" role="img" aria-label="Blue stock market chart"></div>
      <h3>Trading Of Shares</h3>
      <p>Learn how company results move share prices and build a watchlist.</p>
      <div class="more">Read More...</div>
    </article>
    <article class="card">
      <div class="card-photo photo-commodities" role="img" aria-label="Gold commodities trading screen"></div>
      <h3>Trading Of Commodities</h3>
      <p>Understand supply, demand and seasons behind gold, oil and grain markets.</p>
      <div class="more">Read More...</div>
    </article>
    <article class="card">
      <div class="card-photo photo-indices" role="img" aria-label="Financial newspaper with index tables"></div>
      <h3>Trading Of Indices</h3>
      <p>Trade whole markets at once and read the mood of economies.</p>
      <div class="more">Read More...</div>
    </article>
    <article class="card">
      <div class="card-photo photo-currencies" role="img" aria-label="Banknotes of several currencies"></div>
      <h3>Trading Of Currencies</h3>
      <p>Discover how rates and news drive the busiest market in the world.</p>
      <div class="more">Read More...</div>
    </article>
  </div>
</section>

<footer class="site-footer">
  <span>Terms &amp; Conditions</span><span>|</span><span>Privacy Protection</span>
</footer>
</body>
</html>
```